Bref créative
Business Card, Stationary, etc. for a plastic surgeon's office
Brennholt Clinic (Plastic & Reconstructive Surgery)
Use standard fonts
Play with the fonts to see what looks best.
Professional
Gregory T. Brennholt, DO
Plastic Surgeon
475 Corwin Haley Blvd, Ste. 260
Harlow Bay, FL 32590
(Tollmead Business Park)
850-GET-TRIM (850-438-8746)
850-438-FAX5 (850-438-3295)
drbrennholt@brennholtclinic.example
www.brennholtclinic.example
This card, stationary, etc. should look clean and professional with my existing logo purchased from a designer using this sight.
I would like the back of the business card to contain the logo (i.e. Brennholt Clinic in larger letters with logo between the two words with Plastic & Reconstructive Surgery written below the main title with smaller font). Thanks and good luck!!!
logo vector file

```html
<!DOCTYPE html>
<html lang="en">
<head>
<meta charset="utf-8">
<title>Brennholt Clinic — Stationery</title>
<link href="https://fonts.googleapis.com/css2?family=Cormorant+Garamond:wght@500&family=Lato:wght@400;700&display=swap" rel="stylesheet">
<style>
  :root{
    --backdrop:#d9d9d9;
    --paper:#fbfaf7;
    --gold:#b7985a;
    --gold-soft:#d8c59c;
    --ink:#3a3a3a;
    --ink-soft:#7a7a7a;
    --card-black:#1b1b1b;
  }
  *{box-sizing:border-box;margin:0;padding:0}
  html,body{width:1200px;height:1011px;overflow:hidden}
  body{background:var(--backdrop);position:relative;font-family:"Lato",Arial,sans-serif;color:var(--ink)}
  .sheet{position:absolute;background:var(--paper);box-shadow:0 2px 8px rgba(0,0,0,.18)}

  .brand{display:flex;flex-direction:column;align-items:center;color:var(--gold)}
  .brand-name{font-family:"Cormorant Garamond",Georgia,serif;font-weight:500;display:flex;align-items:center;gap:.35em;line-height:1}
  .brand-dot{width:.32em;height:.32em;border-radius:50%;background:var(--gold);display:inline-block}
  .brand-tagline{font-size:8px;letter-spacing:.18em;text-transform:uppercase;margin-top:6px;color:var(--ink-soft)}

  /* Letterhead */
  .letterhead{left:60px;top:60px;width:440px;height:570px}
  .letterhead .brand{position:absolute;top:40px;left:0;right:0}
  .letterhead .brand-name{font-size:30px}
  .letterhead-footer{position:absolute;left:40px;right:40px;bottom:34px;border-top:1px solid var(--gold-soft);padding-top:8px;text-align:center;font-size:7.5px;line-height:1.5;color:var(--ink-soft);letter-spacing:.04em}

  /* Envelope */
  .envelope{left:540px;top:214px;width:600px;height:262px}
  .envelope .brand{position:absolute;top:26px;left:0;right:0}
  .envelope .brand-name{font-size:26px}
  .return-address{position:absolute;left:34px;top:108px;font-size:8px;line-height:1.5;color:var(--ink-soft)}
  .envelope-rules{position:absolute;left:34px;right:34px;bottom:26px}
  .envelope-rules div{height:1px;background:var(--gold-soft);margin-top:4px}

  /* Business cards */
  .card{width:340px;height:194px;top:700px}
  .card-back{left:60px;background:var(--card-black);display:flex;align-items:center;justify-content:center}
  .card-back .brand-name{font-size:32px}
  .card-back .brand-tagline{color:var(--gold-soft)}
  .card-front{left:430px;display:flex;align-items:center;justify-content:center}
  .card-front .brand-name{font-size:32px}

  .card-contact{left:800px}
  .card-contact .brand{position:absolute;top:16px;left:0;right:0}
  .card-contact .brand-name{font-size:22px}
  .card-contact .brand-tagline{font-size:6.5px;margin-top:4px}
  .name-band{position:absolute;left:0;right:0;top:82px;height:24px;background:linear-gradient(90deg,var(--gold),var(--gold-soft));display:flex;align-items:center;padding-left:14px}
  .name-band .person{font-size:10.5px;font-weight:700;color:#2a2a2a;background:var(--paper);padding:3px 8px;letter-spacing:.02em}
  .name-band .role{font-size:8px;color:#fff;margin-left:10px;letter-spacing:.1em;text-transform:uppercase}
  .contact-address{position:absolute;left:14px;top:118px;font-size:7px;line-height:1.55;color:var(--ink-soft)}
  .contact-lines{position:absolute;right:14px;top:118px;font-size:7px;line-height:1.55;color:var(--ink-soft);list-style:none}
  .contact-lines li{display:flex;align-items:center;gap:4px;justify-content:flex-end}
  .contact-lines svg{width:7px;height:7px;fill:var(--gold)}
</style>
</head>
<body>

<section class="sheet letterhead">
  <div class="brand">
    <span class="brand-name">Brennholt Clinic <span class="brand-dot"></span></span>
    <span class="brand-tagline">Plastic &amp; Reconstructive Surgery</span>
  </div>
  <footer class="letterhead-footer">
    475 Corwin Haley Blvd, Ste. 260 · Harlow Bay, FL 32590 · (Tollmead Business Park)<br>
    850-GET-TRIM (850-438-8746) · Fax 850-438-FAX5 (850-438-3295) · www.brennholtclinic.example
  </footer>
</section>

<section class="sheet envelope">
  <div class="brand">
    <span class="brand-name">Brennholt Clinic <span class="brand-dot"></span></span>
    <span class="brand-tagline">Plastic &amp; Reconstructive Surgery</span>
  </div>
  <address class="return-address">
    475 Corwin Haley Blvd, Ste. 260<br>
    Harlow Bay, FL 32590<br>
    (Tollmead Business Park)
  </address>
  <div class="envelope-rules"><div></div><div></div></div>
</section>

<section class="sheet card card-back">
  <div class="brand">
    <span class="brand-name">Brennholt Clinic <span class="brand-dot"></span></span>
    <span class="brand-tagline">Plastic &amp; Reconstructive Surgery</span>
  </div>
</section>

<section class="sheet card card-front">
  <div class="brand">
    <span class="brand-name">Brennholt Clinic <span class="brand-dot"></span></span>
    <span class="brand-tagline">Plastic &amp; Reconstructive Surgery</span>
  </div>
</section>

<section class="sheet card card-contact">
  <div class="brand">
    <span class="brand-name">Brennholt Clinic <span class="brand-dot"></span></span>
    <span class="brand-tagline">Plastic &amp; Reconstructive Surgery</span>
  </div>
  <div class="name-band">
    <span class="person">Gregory T. Brennholt, DO</span>
    <span class="role">Plastic Surgeon</span>
  </div>
  <address class="contact-address">
    475 Corwin Haley Blvd, Ste. 260<br>
    Harlow Bay, FL 32590<br>
    (Tollmead Business Park)
  </address>
  <ul class="contact-lines">
    <li><svg viewBox="0 0 10 10"><path d="M2 0h2l1 3-1.5 1a6 6 0 0 0 2.5 2.5L7 5l3 1v2a2 2 0 0 1-2 2A8 8 0 0 1 0 2a2 2 0 0 1 2-2z"/></svg>850-GET-TRIM (850-438-8746)</li>
    <li><svg viewBox="0 0 10 10"><rect x="1" y="3" width="8" height="6"/><rect x="3" y="0" width="4" height="3"/></svg>850-438-FAX5 (850-438-3295)</li>
    <li><svg viewBox="0 0 10 10"><path d="M0 2h10v6H0zM0 2l5 3.5L10 2" stroke="#fff" stroke-width=".8"/></svg>drbrennholt@brennholtclinic.example</li>
    <li><svg viewBox="0 0 10 10"><circle cx="5" cy="5" r="5"/></svg>www.brennholtclinic.example</li>
  </ul>
</section>

</body>
</html>
```